Harbor Circuits LLC is a Minneapolis / St Paul and surrounding communities computer repair and service company. It serves residential and small businesses. We work primarily with virus removal, data recovery, system baselines, networking, and new system installation. The site should look clean, professional, and easy to navigate.

This wordpress project must be coded and integrated into a wordpress theme for easy upload and maintenance.
Updates

Designers - Please make sure your design is in a wordpress theme so that It can be uploaded.  

Thank you,

Brent 

Target Market(s)

Residential and Small Business

Industry/Entity Type

Residential

Requirements
Must have
• Site Content
1. Main Page should have photos that scroll across, Business Description, Space to run
“Specials” Ads
a. Intuitive Navigation
2. Additional Pages
a. Blog for Computer Repair Articles
b. Testimonials Page
c. Contact Pages
d. Services Page with the ability to put in pricing
3. The site must be clean and professional.
4. Wordpress Theme

```html
<!DOCTYPE html>
<html lang="en">
<head>
<meta charset="utf-8">
<title>Harbor Circuits, LLC — About</title>
<link href="https://fonts.googleapis.com/css2?family=PT+Sans:ital,wght@0,400;0,700;1,400&family=Arimo:wght@400;700&display=swap" rel="stylesheet">
<style>
  :root{
    --page-bg:#ececec;
    --green:#5a9a1e;
    --green-dark:#3e7c15;
    --text:#333333;
    --title:#3a3a3a;
    --card:#ffffff;
    --frame:#cfcfcf;
    --footer:#262626;
    --footer-text:#f2f2f2;
    --photo-light:#e6e6e4;
    --photo-mid:#b9b6b0;
    --muted:#c4c4c4;
  }
  *{box-sizing:border-box;margin:0;padding:0}
  html,body{width:1200px;height:683px;overflow:hidden}
  body{background:var(--page-bg);font-family:"Arimo",Arial,sans-serif;color:var(--text);position:relative}
  .page{position:relative;width:1200px;height:683px;overflow:hidden}

  .backdrop-figure{position:absolute;left:0;top:308px;width:172px;height:313px;
    background:linear-gradient(160deg,#d6d6d6 0%,#9a9a9a 40%,#2a2a2a 75%,#bdbdbd 100%);opacity:.55}

  .section-title{font-family:"PT Sans","Trebuchet MS",sans-serif;font-weight:400;color:var(--green);font-size:25px;line-height:1;position:absolute;white-space:nowrap}

  .photo{background:linear-gradient(135deg,var(--photo-light) 0%,#f7f7f5 45%,var(--photo-mid) 100%);border:5px solid var(--frame);position:absolute}

  .body-text{font-size:10.9px;line-height:17.1px;color:var(--text)}
  .body-text p+p{margin-top:7px}

  .btn{position:absolute;display:inline-block;width:68px;height:21px;border-radius:3px;
    background:linear-gradient(#66b02c,#3f7f14);color:#fff;font-size:10.5px;line-height:19px;text-align:center;text-decoration:none;border:1px solid #3a7512}

  /* about */
  .about-title{left:176px;top:10px}
  .about-photo{left:176px;top:46px;width:160px;height:139px}
  .about-text{position:absolute;left:351px;top:43px;width:442px;text-align:justify}
  .about .btn{left:351px;top:165px}

  /* articles */
  .articles-title{left:176px;top:216px}
  .article{position:absolute;left:176px;width:615px;height:168px;background:var(--card)}
  .article-1{top:254px}
  .article-2{top:434px}
  .article-title{position:absolute;left:9px;top:9px;font-family:"PT Sans","Trebuchet MS",sans-serif;font-weight:700;font-size:17px;line-height:20px;color:var(--title);white-space:nowrap}
  .article-meta{position:absolute;left:9px;top:32px;font-family:"PT Sans","Trebuchet MS",sans-serif;font-size:10.8px;line-height:13px;color:var(--green);white-space:nowrap}
  .article-photo{left:10px;top:57px;width:151px;height:91px}
  .article-text{position:absolute;left:175px;top:56px;width:438px;text-align:left;letter-spacing:-0.1px}
  .article .btn{left:175px;top:133px}

  /* sidebar */
  .promo{position:absolute;left:812px;width:213px;border-radius:4px;overflow:hidden}
  .promo-laptop{top:13px;height:120px;background:linear-gradient(#ffffff,#ededed);border:1px solid #d4d4d4}
  .promo-laptop .headline{position:absolute;left:10px;top:8px;font-family:"PT Sans","Trebuchet MS",sans-serif;color:#222;line-height:1}
  .headline .big{font-size:22px;font-weight:700;display:block}
  .headline .small{font-size:12.5px;display:block;margin-top:1px}
  .headline .mid{font-size:17px;font-weight:700;display:block}
  .promo-laptop .promo-photo{position:absolute;right:0;top:12px;width:112px;height:108px;background:linear-gradient(150deg,#f4f4f4,#8c8c8c 70%,#d8d8d8)}
  .promo-btn{position:absolute;left:11px;top:87px;background:#2a2a2a;color:#fff;font-size:9px;font-weight:700;padding:3px 6px;border-radius:3px}
  .promo-audio{top:147px;height:102px;background:linear-gradient(90deg,#3a2410,#5a3510 45%,#2a1808)}
  .promo-audio .promo-photo{position:absolute;left:0;top:14px;width:86px;height:70px;background:linear-gradient(160deg,#1b1b1b,#4a4a4a 60%,#6aa4c8)}
  .promo-audio .audio-title{position:absolute;left:92px;top:12px;font-family:"PT Sans","Trebuchet MS",sans-serif;font-weight:700;color:#fff;font-size:17px;white-space:nowrap}
  .promo-audio .audio-text{position:absolute;left:92px;top:38px;width:116px;color:#e8dccc;font-size:10px;line-height:17px}
  .promo-audio .audio-link{position:absolute;left:95px;top:78px;color:#fff;font-size:10.5px;font-weight:700}

  .testimonials-title{left:812px;top:263px}
  .testimonial{position:absolute;left:812px;top:301px;width:213px;height:198px;background:#fff;border:1px solid #bdbdbd;border-radius:4px}
  .testimonial-tail{position:absolute;left:966px;top:497px}
  .testimonial-heading{position:absolute;left:12px;top:12px;width:190px;font-family:"PT Sans","Trebuchet MS",sans-serif;font-weight:700;font-size:11.5px;line-height:17px;color:var(--title);white-space:nowrap}
  .quote-mark{position:absolute;font-family:Georgia,serif;font-size:48px;line-height:1;color:var(--muted);font-weight:700}
  .quote-open{left:12px;top:48px}
  .quote-close{left:162px;top:108px}
  .testimonial-text{position:absolute;left:24px;top:66px;width:180px;font-size:10.8px;line-height:17.2px;color:var(--text);white-space:nowrap}
  .reviewer-photo{position:absolute;left:25px;top:145px;width:43px;height:33px;border:1px solid #8ea86b;background:linear-gradient(135deg,#e8d9a8,#c89a4e)}
  .reviewer-name{position:absolute;left:74px;top:145px;font-family:"PT Sans","Trebuchet MS",sans-serif;font-size:12px;color:#111}
  .reviewer-place{position:absolute;left:74px;top:162px;font-family:"PT Sans","Trebuchet MS",sans-serif;font-style:italic;font-size:10.5px;color:var(--green-dark)}

  /* footer */
  .site-footer{position:absolute;left:0;top:621px;width:1200px;height:62px;background:var(--footer);color:var(--footer-text);font-family:"PT Sans","Trebuchet MS",sans-serif;font-size:11px}
  .copyright{position:absolute;left:177px;top:17px}
  .footer-links{position:absolute;left:177px;top:32px}
  .footer-links span{margin:0 9px}
  .footer-links a{color:var(--footer-text);text-decoration:none}
  .footer-brand{position:absolute;left:936px;top:22px;font-weight:700;font-size:13px;color:var(--footer-text);display:flex;align-items:center;gap:6px}
  .footer-brand i{display:inline-block;width:12px;height:12px;border-radius:50%;background:var(--footer-text)}
</style>
</head>
<body>
<div class="page">
  <div class="backdrop-figure" role="img" aria-label="Silhouette of a technician seated at a computer desk"></div>

  <main>
    <section class="about">
      <h1 class="section-title about-title">About Harbor Circuits, LLC</h1>
      <div class="photo about-photo" role="img" aria-label="Smiling technician holding a laptop"></div>
      <div class="body-text about-text">
        <p>There are many variations of passages of Lorem Ipsum available, but the majority fdgvfv suffered alteration in some form, by injected humour, or randomised words which don't look even slightly believable. If you are going to use a passage.</p>
        <p>Lorem Ipsum, you need to be sure there isn't anything embarrassing hidden in the middle of text. All the Lorem Ipsum generators on the Internet tend to repeat predefined chunks as necessary, making this the first true generator on the Internet.</p>
      </div>
      <a class="btn" href="#">Learn More</a>
    </section>

    <section class="articles">
      <h2 class="section-title articles-title">Computer Repair Articles</h2>
      <article class="article article-1">
        <h3 class="article-title">Purchase as many Pay-as-you-go Credits</h3>
        <div class="article-meta">Date: 28.08.12 Tags: Computer, repaor, Virus Removal</div>
        <div class="photo article-photo" role="img" aria-label="Smiling technician with a laptop"></div>
        <p class="body-text article-text">There are many variations of passages of Lorem Ipsum available, but the majority have suffered alteration in some form, by injected humour, or randomised words which don't look even slightly believable. If you are going to use a passage. , or randomised words which don't look even slightly believable. If you are going to use a passage.</p>
        <a class="btn" href="#">Learn More</a>
      </article>
      <article class="article article-2">
        <h3 class="article-title">Purchase as many Pay-as-you-go Credits</h3>
        <div class="article-meta">Date: 28.08.12 Tags: Computer, repaor, Virus Removal</div>
        <div class="photo article-photo" role="img" aria-label="Smiling technician with a laptop"></div>
        <p class="body-text article-text">There are many variations of passages of Lorem Ipsum available, but the majority have suffered alteration in some form, by injected humour, or randomised words which don't look even slightly believable. If you are going to use a passage. , or randomised words which don't look even slightly believable. If you are going to use a passage.</p>
        <a class="btn" href="#">Learn More</a>
      </article>
    </section>
  </main>

  <aside>
    <div class="promo promo-laptop">
      <div class="promo-photo" role="img" aria-label="Open silver laptop"></div>
      <div class="headline">
        <span class="big">powerful</span>
        <span class="small">performance</span>
        <span class="mid">and attractive</span>
        <span class="mid">designs</span>
      </div>
      <span class="promo-btn">View more</span>
    </div>
    <div class="promo promo-audio">
      <div class="promo-photo" role="img" aria-label="Portable MP3 player"></div>
      <div class="audio-title">MP3/WMA/REC</div>
      <div class="audio-text">Nulla facilisi. Vivamus ut justo nulla, sed lacinia</div>
      <div class="audio-link">Click Here &raquo;</div>
    </div>

    <h2 class="section-title testimonials-title">Testimonials</h2>
    <div class="testimonial">
      <div class="testimonial-heading">LOREM IPSUM DOLOR CONSECTE<br>TUR ADIPSCING</div>
      <span class="quote-mark quote-open">&ldquo;</span>
      <p class="testimonial-text">Lorem ipsum dolor sit amet, ons<br>ectetur adipiscing elit. Quisque<br>quis tortor euismod ante ullam-<br>corper consectetur id et est.</p>
      <span class="quote-mark quote-close">&rdquo;</span>
      <div class="reviewer-photo" role="img" aria-label="Customer at a laptop"></div>
      <div class="reviewer-name">LOREM IPSUM</div>
      <div class="reviewer-place">USA, WILLINTONG</div>
    </div>
    <svg class="testimonial-tail" width="34" height="24" viewBox="0 0 34 24" aria-hidden="true">
      <path d="M4 1 L32 1 L2 22 Z" fill="#fff"/>
      <path d="M32 1.5 L2 22 L5 2" fill="none" stroke="#bdbdbd" stroke-width="1"/>
    </svg>
  </aside>

  <footer class="site-footer">
    <div class="copyright">&copy; 2012, All right reserved by Harbor Circuits, LLC</div>
    <nav class="footer-links"><a href="#">Terms &amp; Condition</a><span>|</span><a href="#">Privacy Policy</a></nav>
    <div class="footer-brand"><i></i>Harbor Circuits</div>
  </footer>
</div>
</body>
</html>
```